Brightgate Business Card Design

Name Marisa Okonduye
Title Mortgage Originator
Office (800) 555-0142 x65
Direct (240) 555-0187
Email mokonduye@brightgatehomes.example
NMLS 5830472
Licensed MD

Name Deron Plummer
Title Mortgage Originator
Office (800) 555-0142 x66
Direct (404) 555-0163
Email dplummer@brightgatehomes.example
NMLS 5917360
Licensed MD

Name Lakendra Burton
Title Mortgage Originator
Office (800) 555-0142 x67
Direct (443) 555-0129
Email burtonlakendra@mailbox.example
NMLS 5372619
Licensed MD

Name Samir Qudwaheli
Title Mortgage Originator
Office (800) 555-0142 x32
Direct (571) 555-0176
Email squdwaheli@brightgatehomes.example
NMLS 4068259
Licensed MD

```html
<!DOCTYPE html>
<html lang="en">
<head>
<meta charset="utf-8">
<title>Brightgate Business Cards</title>
<link href="https://fonts.googleapis.com/css2?family=Montserrat:wght@400;500;700&display=swap" rel="stylesheet">
<style>
  :root {
    --backdrop: #c4c4c4;
    --card: #ffffff;
    --gold: #e3aa46;
    --navy: #2a3886;
    --ink: #3a3a3a;
  }
  * { margin: 0; padding: 0; box-sizing: border-box; }
  html, body { width: 1200px; height: 915px; overflow: hidden; }
  body {
    background: var(--backdrop);
    font-family: "Montserrat", Arial, sans-serif;
    position: relative;
  }
  .card {
    position: absolute;
    width: 510px;
    height: 291px;
    background: var(--card);
    border-radius: 22px;
    overflow: hidden;
  }
  .card--a { left: 70px; top: 120px; }
  .card--b { left: 620px; top: 122px; }
  .card--c { left: 70px; top: 474px; }
  .card--d { left: 620px; top: 477px; }

  .brand {
    position: absolute;
    left: 32px;
    top: 62px;
    display: flex;
    align-items: center;
    gap: 8px;
  }
  .brand__dot {
    width: 18px; height: 18px;
    border-radius: 50%;
    background: var(--gold);
  }
  .brand__name {
    font-weight: 700;
    font-size: 22px;
    color: var(--navy);
  }

  .person {
    position: absolute;
    left: 31px;
    top: 128px;
    z-index: 1;
  }
  .person__name {
    font-weight: 700;
    font-size: 20.5px;
    letter-spacing: 0.2px;
    color: var(--gold);
    text-transform: uppercase;
    line-height: 1.1;
  }
  .person__title {
    font-size: 14px;
    color: var(--ink);
    margin-top: 1px;
  }
  .person__rule {
    width: 10px; height: 1.5px;
    background: var(--gold);
    margin: 12px 0 10px;
  }
  .contact { list-style: none; }
  .contact li {
    display: flex;
    align-items: center;
    gap: 6px;
    font-size: 12.2px;
    color: var(--ink);
    height: 21px;
    white-space: nowrap;
  }
  .contact svg { width: 10px; height: 10px; flex: none; fill: var(--navy); }

  .photo {
    position: absolute;
    right: 0;
    top: 28px;
    width: 160px;
    height: 233px;
    border-radius: 40px 0 0 0;
  }
  .photo--warm { background: linear-gradient(180deg, #f4eee9 0%, #a06a4a 55%, #5d5a35 100%); }
  .photo--suit { background: linear-gradient(180deg, #f4f1ee 0%, #6e4a37 45%, #233150 100%); }
  .photo--blush { background: linear-gradient(180deg, #f5efe9 0%, #9a6a45 50%, #ecc9b4 100%); }
  .photo--sage { background: linear-gradient(180deg, #f3f3f1 0%, #9a8470 45%, #a4a390 100%); }

  .footer {
    position: absolute;
    left: 0; bottom: 0;
    width: 510px; height: 30px;
  }
  .footer__band { fill: var(--navy); }
  .footer__tab { fill: var(--gold); }
  .license {
    position: absolute;
    right: 14px;
    bottom: 7px;
    font-size: 12.6px;
    color: #ffffff;
    letter-spacing: 0.2px;
    white-space: nowrap;
  }
  .license__sep { margin: 0 8px; }
</style>
</head>
<body>

<svg width="0" height="0" style="position:absolute">
  <defs>
    <symbol id="icon-phone" viewBox="0 0 10 10"><path d="M2.2 0.5 L3.6 2.4 L2.8 3.4 C3.4 4.8 5.2 6.6 6.6 7.2 L7.6 6.4 L9.5 7.8 L8.6 9.4 C5 9.6 0.4 5 0.6 1.4 Z"/></symbol>
    <symbol id="icon-mobile" viewBox="0 0 10 10"><path d="M2.5 0 H7.5 V10 H2.5 Z M3.5 1.2 V7.8 H6.5 V1.2 Z M4.6 8.4 H5.4 V9.2 H4.6 Z"/></symbol>
    <symbol id="icon-mail" viewBox="0 0 10 10"><path d="M0 2 H10 V8.5 H0 Z M0.9 2.6 L5 5.8 L9.1 2.6 Z"/></symbol>
  </defs>
</svg>

<article class="card card--a">
  <div class="brand"><span class="brand__dot"></span><span class="brand__name">Brightgate</span></div>
  <div class="person">
    <h2 class="person__name">Marisa Okonduye</h2>
    <p class="person__title">Mortgage Originator</p>
    <div class="person__rule"></div>
    <ul class="contact">
      <li><svg><use href="#icon-phone"/></svg>(800) 555-0142 x65</li>
      <li><svg><use href="#icon-mobile"/></svg>(240) 555-0187</li>
      <li><svg><use href="#icon-mail"/></svg>mokonduye@brightgatehomes.example</li>
    </ul>
  </div>
  <div class="photo photo--warm" role="img" aria-label="Portrait photo of Marisa Okonduye"></div>
  <svg class="footer" viewBox="0 0 510 30"><rect class="footer__band" x="0" y="19" width="300" height="11"/><polygon class="footer__tab" points="266,30 292,0 510,0 510,30"/></svg>
  <p class="license">NMLS 5830472<span class="license__sep">I</span>Licensed MD</p>
</article>

<article class="card card--b">
  <div class="brand"><span class="brand__dot"></span><span class="brand__name">Brightgate</span></div>
  <div class="person">
    <h2 class="person__name">Deron Plummer</h2>
    <p class="person__title">Mortgage Originator</p>
    <div class="person__rule"></div>
    <ul class="contact">
      <li><svg><use href="#icon-phone"/></svg>(800) 555-0142 x66</li>
      <li><svg><use href="#icon-mobile"/></svg>(404) 555-0163</li>
      <li><svg><use href="#icon-mail"/></svg>dplummer@brightgatehomes.example</li>
    </ul>
  </div>
  <div class="photo photo--suit" role="img" aria-label="Portrait photo of Deron Plummer"></div>
  <svg class="footer" viewBox="0 0 510 30"><rect class="footer__band" x="0" y="19" width="300" height="11"/><polygon class="footer__tab" points="266,30 292,0 510,0 510,30"/></svg>
  <p class="license">NMLS 5917360<span class="license__sep">I</span>Licensed MD</p>
</article>

<article class="card card--c">
  <div class="brand"><span class="brand__dot"></span><span class="brand__name">Brightgate</span></div>
  <div class="person">
    <h2 class="person__name">Lakendra Burton</h2>
    <p class="person__title">Mortgage Originator</p>
    <div class="person__rule"></div>
    <ul class="contact">
      <li><svg><use href="#icon-phone"/></svg>(800) 555-0142 x67</li>
      <li><svg><use href="#icon-mobile"/></svg>(443) 555-0129</li>
      <li><svg><use href="#icon-mail"/></svg>burtonlakendra@mailbox.example</li>
    </ul>
  </div>
  <div class="photo photo--blush" role="img" aria-label="Portrait photo of Lakendra Burton"></div>
  <svg class="footer" viewBox="0 0 510 30"><rect class="footer__band" x="0" y="19" width="300" height="11"/><polygon class="footer__tab" points="266,30 292,0 510,0 510,30"/></svg>
  <p class="license">NMLS 5372619<span class="license__sep">I</span>Licensed MD</p>
</article>

<article class="card card--d">
  <div class="brand"><span class="brand__dot"></span><span class="brand__name">Brightgate</span></div>
  <div class="person">
    <h2 class="person__name">Samir Qudwaheli</h2>
    <p class="person__title">Mortgage Originator</p>
    <div class="person__rule"></div>
    <ul class="contact">
      <li><svg><use href="#icon-phone"/></svg>(800) 555-0142 x32</li>
      <li><svg><use href="#icon-mobile"/></svg>(571) 555-0176</li>
      <li><svg><use href="#icon-mail"/></svg>squdwaheli@brightgatehomes.example</li>
    </ul>
  </div>
  <div class="photo photo--sage" role="img" aria-label="Portrait photo of Samir Qudwaheli"></div>
  <svg class="footer" viewBox="0 0 510 30"><rect class="footer__band" x="0" y="19" width="300" height="11"/><polygon class="footer__tab" points="266,30 292,0 510,0 510,30"/></svg>
  <p class="license">NMLS 4068259<span class="license__sep">I</span>Licensed MD</p>
</article>

</body>
</html>
```